Product Marketing Slick / Product Brief. 1 sheet now then an additional 2 plus more in the future.

We need to create 1 page product sheets that will be used for marketing purposes.
The products we are selling are network security and network compliance for PCI, HIPAA and GDPR.
We will essentially be doing all of the consulting to make their networks secure, then on a daily basis be scanning and validating that all of the government requirements are being met for compliance.
We dont want to make this too technical so its more of a page that will discuss in general terms what we do and why its important for them to have our services.
***Note There will be a total of Three Sheets, this project is for the first one and can be for any one of the products. HIPAA Compliance , PCI Compliance or GDPR Compliance.
We will contract with you to do the additional 2 pages and probably more if we select your design.
Target Market(s)
Medical, Hospitality
Industry/Entity Type
Medical
Colors
Designer to choose colors to be used in the design.
Look and feel

```html
<!DOCTYPE html>
<html lang="en">
<head>
<meta charset="utf-8">
<title>Veridora – HIPAA Compliance Product Sheet</title>
<link rel="stylesheet" href="https://fonts.googleapis.com/css2?family=Montserrat:wght@600;700;800&family=Open+Sans:wght@400;600;700&display=swap">
<style>
  :root {
    --brand-blue: #1a7cc4;
    --deep-blue: #0b3f78;
    --night-blue: #08264a;
    --brand-green: #7dbb2f;
    --leaf-green: #5aa22a;
    --ink: #333a40;
    --paper: #ffffff;
    --mist: #e9f3fb;
  }
  * { box-sizing: border-box; margin: 0; padding: 0; }
  html, body { width: 778px; height: 1200px; overflow: hidden; background: var(--paper); }
  body { font-family: "Open Sans", Arial, sans-serif; color: var(--ink); }

  .sheet { position: relative; width: 778px; height: 1200px; overflow: hidden; background: var(--paper); }

  .hero { position: absolute; top: 0; left: 0; width: 778px; height: 590px; }
  .hero svg { display: block; }

  .brand-tab {
    position: absolute; top: 28px; left: 30px;
    display: flex; align-items: center; gap: 10px;
    padding: 12px 20px; background: var(--brand-green);
  }
  .brand-dot { width: 26px; height: 26px; border-radius: 50%; background: var(--paper); }
  .brand-name {
    font-family: "Montserrat", Arial, sans-serif; font-weight: 700;
    font-size: 22px; letter-spacing: 2px; color: var(--paper);
  }
  .brand-tagline {
    position: absolute; top: 82px; left: 30px; width: 228px;
    padding: 4px 20px; background: var(--paper);
    font-size: 10px; color: var(--leaf-green); letter-spacing: .5px;
  }

  .content { position: absolute; top: 585px; left: 48px; right: 48px; }
  .pillars {
    font-family: "Montserrat", Arial, sans-serif; font-weight: 800;
    font-size: 34px; color: var(--brand-blue); letter-spacing: 1px;
    display: flex; align-items: center; gap: 18px;
  }
  .pillars .dot { width: 11px; height: 11px; border-radius: 50%; background: var(--brand-green); }
  .slogan {
    margin-top: 18px;
    font-family: "Montserrat", Arial, sans-serif; font-weight: 700;
    font-size: 27px; color: var(--leaf-green);
  }
  .act-title { margin-top: 14px; font-weight: 700; font-size: 16px; color: var(--ink); line-height: 1.35; }
  .body-copy p { margin-top: 10px; font-size: 13px; line-height: 1.55; color: var(--ink); }

  .footer { position: absolute; left: 0; bottom: 0; width: 778px; height: 190px; }
  .footer svg { position: absolute; top: 0; left: 0; }
  .contact {
    position: absolute; left: 48px; top: 62px;
    color: var(--paper); font-size: 12px; line-height: 1.6;
  }
  .contact h3 { font-size: 14px; font-weight: 700; margin-bottom: 2px; }
  .contact-line { display: flex; align-items: center; gap: 7px; }
  .contact-line svg { position: static; }
  .footer-brand {
    position: absolute; right: 48px; top: 82px;
    display: flex; align-items: center; gap: 10px;
  }
  .footer-brand .brand-dot { width: 30px; height: 30px; }
  .footer-brand .brand-name { font-size: 24px; }
  .web { position: absolute; right: 48px; bottom: 22px; color: var(--paper); font-size: 12px; }
</style>
</head>
<body>
<main class="sheet">

  <header class="hero">
    <svg width="778" height="590" viewBox="0 0 778 590">
      <defs>
        <linearGradient id="heroTone" x1="0" y1="0" x2="1" y2="1">
          <stop offset="0" stop-color="#cfe4f4"/>
          <stop offset=".45" stop-color="#3d86c4"/>
          <stop offset="1" stop-color="#08264a"/>
        </linearGradient>
      </defs>
      <rect class="hero-photo" role="img" aria-label="Photo of a businessman in a suit touching a glowing digital network interface" x="0" y="0" width="778" height="560" fill="url(#heroTone)"/>
      <path d="M0 440 C 200 540, 480 560, 778 470 L778 590 L0 590 Z" fill="var(--paper)"/>
      <path d="M0 430 C 200 525, 480 545, 778 455" fill="none" stroke="var(--brand-green)" stroke-width="6"/>
      <path d="M0 415 C 210 505, 470 525, 778 438" fill="none" stroke="var(--brand-blue)" stroke-width="3"/>
      <path d="M0 448 C 220 540, 490 565, 778 478" fill="none" stroke="var(--brand-blue)" stroke-width="2" opacity=".6"/>
    </svg>
    <div class="brand-tab">
      <span class="brand-dot"></span>
      <span class="brand-name">VERIDORA</span>
    </div>
    <div class="brand-tagline">network security &amp; compliance</div>
  </header>

  <section class="content">
    <h1 class="pillars">
      <span>SMART</span><span class="dot"></span>
      <span>SIMPLE</span><span class="dot"></span>
      <span>SAFE</span><span class="dot"></span>
      <span>SECURE</span>
    </h1>
    <h2 class="slogan">We worry, so you don't have to.</h2>
    <p class="act-title">Health Insurance Portability &amp; Accountability Act. (HIPAA)<br>
      HIPAA (Health Insurance Portability &amp; Accountability Act.)</p>
    <div class="body-copy">
      <p>Every day we scan, test and validate your network so patient records stay private and your practice stays compliant. Our team handles the consulting, the setup and the daily checks, giving your staff more time to focus on care instead of paperwork, audits and the fear of a costly data breach.</p>
      <p>Compliance is not a one time task. Rules change and threats grow, so we keep watch around the clock and report back in plain language.</p>
      <p>Do you really want to leave all of the complexities of HIPAA and PCI compliance to chance? Let us take it off your plate. We'll have your team up and running fast so you never have to think about it again.</p>
    </div>
  </section>

  <footer class="footer">
    <svg width="778" height="190" viewBox="0 0 778 190">
      <path d="M0 40 C 260 0, 520 0, 778 30 L778 190 L0 190 Z" fill="var(--brand-blue)"/>
      <path d="M0 40 C 260 0, 520 0, 778 30" fill="none" stroke="var(--brand-green)" stroke-width="5"/>
    </svg>
    <div class="contact">
      <h3>Contact Info</h3>
      <div>Veridora Inc.</div>
      <div class="contact-line">
        <svg width="11" height="14" viewBox="0 0 11 14"><path d="M5.5 0a5.5 5.5 0 0 0-5.5 5.5C0 9.5 5.5 14 5.5 14S11 9.5 11 5.5A5.5 5.5 0 0 0 5.5 0zm0 7.5a2 2 0 1 1 0-4 2 2 0 0 1 0 4z" fill="var(--paper)"/></svg>
        1820 Harbor Lane, Suite 4, Fairview, OR 97024
      </div>
      <div class="contact-line">
        <svg width="12" height="12" viewBox="0 0 12 12"><path d="M2.4 0l2 2.6-1.1 1.5a7 7 0 0 0 4.6 4.6l1.5-1.1L12 9.6 10.6 12C4.8 11.6.4 7.2 0 1.4z" fill="var(--paper)"/></svg>
        Phone: 555-014-2291
      </div>
      <div class="contact-line">
        <svg width="13" height="10" viewBox="0 0 13 10"><rect x=".5" y=".5" width="12" height="9" fill="none" stroke="var(--paper)"/><path d="M.5.5l6 5 6-5" fill="none" stroke="var(--paper)"/></svg>
        E-mail: hello@veridora.example
      </div>
    </div>
    <div class="footer-brand">
      <span class="brand-dot"></span>
      <span class="brand-name">VERIDORA</span>
    </div>
    <div class="web">www.veridora.example</div>
  </footer>

</main>
</body>
</html>
```